Home Page Redesign for Pet Website

Looking to redesign the home page of our WORDPRESS website which will be renamed The Critter Cover Handbook 2015.

Looking for clean design which communicates clarity.
Updates

This is for a Wordpress site.

Please note that the design MUST include the content which is shown in the table in the brief!

Hi Thanks for the designs so far. We have just updated the brief to provide more information and clarify a few issues. We have also now included a couple of layout suggestions. They are just suggestions but it should give you a better idea of what we are looking for. And we have just increased the budget for 1st place by £120. Please feel free to message me if you have any questions. Many thanks. Maud

Please note that the new brief is in a file dated 25 Jan!

Reason: We have extended the deadline so we can continue working with the designers who have submitted designs we like. If you have any new designs please submit them by the original deadline of 7.37pm this evening (GMT). We are planning to make our final decision by Friday this week.

Target Market(s)

UK pet owners. All ages but largest age group is 35-50.

Industry/Entity Type

Insurance

Requirements
Must have
• Three clear content groups - LEARN, RESEARCH, CAMPAIGN (see brief for more details).
Stock photos with dogs and cats
Use current colour scheme
Must work with existing inner pages.
Existing font.. but 1pt larger
See brief for more details
Should not have
• Logo
Content from Existing Page (except for footer content... and menu headings).

```html
<!DOCTYPE html>
<html lang="en">
<head>
<meta charset="utf-8">
<title>The Critter Cover Handbook 2015</title>
<link href="https://fonts.googleapis.com/css2?family=Fredoka:wght@400;600&family=Cabin:wght@400;500&family=Arimo:wght@400;700&display=swap" rel="stylesheet">
<style>
:root{
  --orange:#f07318;
  --ink:#333333;
  --text:#222222;
  --header:#2b2b2b;
  --learn:#1b78c4;
  --research:#8a2f9b;
  --campaign:#19b3d3;
  --green:#3a8f4a;
  --card:#f4f4f4;
  --line:#dddddd;
  --band:#1a7fd1;
  --white:#ffffff;
}
*{box-sizing:border-box;margin:0;padding:0}
html,body{width:734px;height:1200px;overflow:hidden;background:var(--white)}
body{font-family:Arimo,Arial,sans-serif;color:var(--text)}
.page{position:relative;width:734px;height:1200px;overflow:hidden}
.abs{position:absolute}

/* header */
.site-header{position:absolute;left:0;top:0;width:734px;height:52px;background:var(--header)}
.brand{position:absolute;left:86px;top:10px;line-height:1.1}
.brand .l1{font-family:Fredoka,sans-serif;font-weight:600;color:var(--orange);font-size:16px;display:block;white-space:nowrap}
.brand .l2{font-family:Cabin,sans-serif;color:var(--white);font-size:10px;display:block;margin-left:1px}
.search{position:absolute;left:508px;top:10px;width:140px;height:14px;background:var(--white);font-size:8px;color:#555;padding:2px 5px}
.search svg{position:absolute;right:4px;top:2px}
.nav{position:absolute;top:32px;left:0;width:734px;font-size:8.5px;color:var(--white)}
.nav span{position:absolute;top:0;white-space:nowrap}
.nav .active::after{content:"";position:absolute;left:-5px;right:-5px;top:15px;height:3px;background:var(--campaign)}

/* hero */
.hero{position:absolute;left:0;top:52px;width:734px;height:255px;background:linear-gradient(#eeeeee 0%,#ffffff 14%,#ffffff 70%,#dcdcdc 100%)}
.hero-title{position:absolute;left:86px;top:46px;font-family:Fredoka,sans-serif;font-weight:600;font-size:30px;line-height:35px;white-space:nowrap}
.hero-title .a{color:var(--orange);display:block}
.hero-title .b{color:var(--ink);display:block}
.hero-sub{position:absolute;left:88px;top:125px;font-family:Cabin,sans-serif;font-size:14px;line-height:21px;color:#333;letter-spacing:.2px}
.hero-photo{position:absolute;left:336px;top:24px;width:312px;height:214px;border-radius:55% 35% 10px 60% / 45% 40% 10px 25%;background:radial-gradient(ellipse at 60% 45%,#8a6a4a 0%,#6e5238 35%,#bdb4aa 72%,rgba(255,255,255,0) 100%)}

/* columns */
.card{position:absolute;top:351px;width:169px;height:337px;background:var(--card);border:1px solid var(--line);border-radius:6px}
.card svg.tab{position:absolute;left:-1px;top:-1px}
.card .tab-label{position:absolute;left:0;top:2px;width:169px;text-align:center;font-family:Cabin,sans-serif;font-size:21px;color:var(--white)}
.card h3{position:absolute;top:53px;left:0;width:169px;text-align:center;font-family:Cabin,sans-serif;font-weight:400;font-size:12.5px;color:#222}
.learn{left:85px}.research{left:284px}.campaign{left:480px}
.ticks{position:absolute;left:9px;top:82px;list-style:none;font-size:7.4px;color:#222}
.ticks li{position:relative;padding-left:11px;height:20.3px;line-height:9px}
.ticks svg{position:absolute;left:0;top:1px}
.research-body{position:absolute;left:15px;top:82px;font-size:7.4px;line-height:10.1px;color:#222;width:145px}
.research-body .in{padding-left:14px;display:block}
.research-body b{display:block}
.research-body p{margin-bottom:7px}
.campaign-body{position:absolute;left:17px;top:81px;font-size:7.4px;line-height:10px;width:135px}

/* lower */
.section-h{font-family:Fredoka,sans-serif;font-weight:400;font-size:20px;color:var(--orange)}
.features{position:absolute;left:88px;top:762px;list-style:none;font-size:7.4px;color:#222}
.features li{height:20.3px}
.features li::before{content:"+ ";}
.disclaimer{position:absolute;left:88px;top:916px;width:345px;font-size:7.4px;line-height:11.2px}
.divider{position:absolute;left:453px;top:735px;width:1px;height:240px;background:#cccccc}
.bio-h{color:var(--green)}
.bio-photo{position:absolute;left:481px;top:763px;width:55px;height:56px;background:linear-gradient(135deg,#6f5a4c,#3a302a)}
.bio-card{position:absolute;left:545px;top:765px;font-size:5.4px;line-height:7px;color:#222}
.bio-card .name{font-family:Cabin,sans-serif;font-size:7px}
.bio-card .name small{font-size:3.5px;color:#aaa}
.bio-card .role em{font-style:normal;color:var(--orange)}
.chips{display:flex;gap:2px;margin-top:2px}
.chips span{display:block;height:5px;border-radius:1px}
.bio-text{position:absolute;left:480px;top:828px;width:165px;font-size:7.4px;line-height:11.2px}
.bio-text p{margin-bottom:11px}

/* footer */
.site-footer{position:absolute;left:0;top:1010px;width:734px;height:168px;background:var(--header)}
.fb-box{position:absolute;left:92px;top:1027px;width:148px;height:131px;border:1px solid #555;background:#262626;color:#ddd;font-size:5.5px}
.fb-box .title{position:absolute;left:4px;top:3px;font-weight:700;font-size:6px}
.fb-box .sep{position:absolute;left:4px;right:4px;height:1px;background:#555}
.fb-box .mark{position:absolute;left:7px;top:22px;width:20px;height:20px;background:#4a6aa8}
.fb-box .page-name{position:absolute;left:32px;top:22px;font-weight:700;font-size:6px;color:#fff}
.fb-box .like{position:absolute;left:34px;top:32px;width:22px;height:9px;background:#ddd;color:#333;font-size:5px;text-align:center;line-height:9px}
.fb-box .count{position:absolute;left:7px;top:52px;font-size:4.5px;color:#999}
.faces{position:absolute;left:8px;top:64px;display:grid;grid-template-columns:repeat(5,23px);gap:3px 2px}
.faces span{width:23px;height:23px;background:#777}
.fb-box .foot{position:absolute;left:8px;bottom:3px;font-size:4.5px}
.tw-box{position:absolute;left:279px;top:1028px;width:148px;height:136px;background:#1f96b3}
.tw-head{position:absolute;left:25px;top:4px;color:#fff;font-size:6px;line-height:7.5px;white-space:nowrap}
.tw-head b{font-size:6.2px}
.tw-avatar{position:absolute;left:4px;top:4px;width:17px;height:17px;background:#ddd;border-radius:2px}
.tw-feed{position:absolute;left:4px;top:25px;width:140px;height:93px;background:#fff;font-size:5.8px;line-height:6.8px;color:#222}
.tweet{padding:3px 4px;border-bottom:1px solid #ddd;height:31px}
.tweet .who{color:#4a8bc0}
.tweet a{color:#1a77c9;text-decoration:none}
.tweet .meta{font-size:4px;color:#4a8bc0;display:block}
.tw-foot{position:absolute;left:6px;top:122px;color:#fff;font-size:6.4px;font-weight:700;width:136px}
.tw-foot span{position:absolute;right:0;top:1px;font-weight:400;font-size:5.5px}
.follow-h{position:absolute;left:452px;top:1030px;font-family:Cabin,sans-serif;font-size:21px;color:var(--white)}
.btn{position:absolute;left:453px;height:10px;font-size:5.8px;line-height:10px;padding:0 4px;border-radius:2px}
.btn.tw{top:1061px;background:#e6e6e6;color:#222;width:94px}
.btn.fb{top:1075px;background:#3b5998;color:#fff;width:28px}
.btn.gp{top:1088px;background:#fff;color:#222;width:46px;text-align:center}
.flinks{position:absolute;left:454px;top:1110px;color:#fff;font-size:7.4px;line-height:13.6px}
.band{position:absolute;left:0;top:1178px;width:734px;height:22px;background:var(--band);color:#fff;font-size:7.4px;text-align:center;line-height:22px}
</style>
</head>
<body>
<div class="page">

  <header class="site-header">
    <div class="brand"><span class="l1">The Critter Cover</span><span class="l2">Handbook 2015</span></div>
    <div class="search">Search tab
      <svg width="9" height="9" viewBox="0 0 9 9"><circle cx="3.8" cy="3.8" r="2.7" fill="none" stroke="#8a2f9b" stroke-width="1.3"/><line x1="5.8" y1="5.8" x2="8.2" y2="8.2" stroke="#8a2f9b" stroke-width="1.3"/></svg>
    </div>
    <nav class="nav">
      <span class="active" style="left:247px">Home</span>
      <span style="left:292px">Pet Insurance Reviews</span>
      <span style="left:399px">Providers A-Z</span>
      <span style="left:472px">Pet Insurance Policies</span>
      <span style="left:577px">Surveys</span>
      <span style="left:629px">More</span>
    </nav>
  </header>

  <section class="hero">
    <div class="hero-photo" role="img" aria-label="Photo of a brindle dog lying down with a black and white cat in front of it"></div>
    <h1 class="hero-title"><span class="a">The Critter Cover</span><span class="b">Handbook 2015</span></h1>
    <p class="hero-sub">Independent Unbiased Information<br>for Fellow Pet Owners</p>
  </section>

  <!-- Learn -->
  <div class="card learn">
    <svg class="tab" width="169" height="48" viewBox="0 0 169 48"><path d="M0,6 Q0,0 6,0 H163 Q169,0 169,6 V31 H104 Q90,33 84.5,46 Q79,33 65,31 H0 Z" fill="var(--learn)"/></svg>
    <div class="tab-label">Learn</div>
    <h3>About Pet Insurance</h3>
    <ul class="ticks">
      <li><svg width="7" height="6" viewBox="0 0 7 6"><path d="M0.5,3 L2.6,5.2 L6.5,0.6" fill="none" stroke="#4a7cb0" stroke-width="1.4"/></svg>Introduction to Pet Insurance</li>
      <li><svg width="7" height="6" viewBox="0 0 7 6"><path d="M0.5,3 L2.6,5.2 L6.5,0.6" fill="none" stroke="#4a7cb0" stroke-width="1.4"/></svg>Vet Fees Cover Types</li>
      <li><svg width="7" height="6" viewBox="0 0 7 6"><path d="M0.5,3 L2.6,5.2 L6.5,0.6" fill="none" stroke="#4a7cb0" stroke-width="1.4"/></svg>What to Consider before Buying</li>
      <li><svg width="7" height="6" viewBox="0 0 7 6"><path d="M0.5,3 L2.6,5.2 L6.5,0.6" fill="none" stroke="#4a7cb0" stroke-width="1.4"/></svg>Ten Popular Pet Insurance Providers</li>
      <li><svg width="7" height="6" viewBox="0 0 7 6"><path d="M0.5,3 L2.6,5.2 L6.5,0.6" fill="none" stroke="#4a7cb0" stroke-width="1.4"/></svg>Confused by Pet Insurance:&nbsp; Start Here!</li>
      <li><svg width="7" height="6" viewBox="0 0 7 6"><path d="M0.5,3 L2.6,5.2 L6.5,0.6" fill="none" stroke="#4a7cb0" stroke-width="1.4"/></svg>Third Party Liability Insurance</li>
      <li style="height:29.5px"><svg width="7" height="6" viewBox="0 0 7 6"><path d="M0.5,3 L2.6,5.2 L6.5,0.6" fill="none" stroke="#4a7cb0" stroke-width="1.4"/></svg>Six Vet Fees Pet Insurance Companies<br>Won't Pay!</li>
      <li><svg width="7" height="6" viewBox="0 0 7 6"><path d="M0.5,3 L2.6,5.2 L6.5,0.6" fill="none" stroke="#4a7cb0" stroke-width="1.4"/></svg>Why Cheap Pet Insurance is Risky</li>
      <li><svg width="7" height="6" viewBox="0 0 7 6"><path d="M0.5,3 L2.6,5.2 L6.5,0.6" fill="none" stroke="#4a7cb0" stroke-width="1.4"/></svg>Why Your Pets Vet History is Important</li>
    </ul>
  </div>

  <!-- Research -->
  <div class="card research">
    <svg class="tab" width="169" height="48" viewBox="0 0 169 48"><path d="M0,6 Q0,0 6,0 H163 Q169,0 169,6 V31 H104 Q90,33 84.5,46 Q79,33 65,31 H0 Z" fill="var(--research)"/></svg>
    <div class="tab-label">Research</div>
    <h3>UK Pet Insurance Policies</h3>
    <div class="research-body">
      <p>Analysis, Customer Reviews and Full Details of All UK Policies</p>
      <div style="margin-bottom:7px">
        <span class="in">Paw Pals</span>
        <span class="in">Argent</span>
        <span class="in">Straight Path</span>
        <span class="in">R&amp;T</span>
        <span class="in">Hale Pets</span>
        <b>Coverwell</b>
        <span class="in">Hart &amp; Lowe</span>
        <span class="in">LQ=</span>
        <span class="in">Hound Society</span>
        <span class="in">P&amp;K</span>
        <span class="in">Beyond Cover</span>
        <b>Tailplan</b>
        <span class="in">Bramley's</span>
        <b>Fenwick Mart</b>
        <span class="in">Cobalt Money</span>
        <span class="in">Other Providers</span>
      </div>
      <p>Search our database for policies matching your criteria</p>
      <p>Compare claims experiences&nbsp; for pet insurance providers</p>
    </div>
  </div>

  <!-- Campaign -->
  <div class="card campaign">
    <svg class="tab" width="169" height="48" viewBox="0 0 169 48"><path d="M0,6 Q0,0 6,0 H163 Q169,0 169,6 V31 H104 Q90,33 84.5,46 Q79,33 65,31 H0 Z" fill="var(--campaign)"/></svg>
    <div class="tab-label">Campaign</div>
    <h3>For Fairer Pet Insurance</h3>
    <p class="campaign-body">This section will contain three para graphs of text.</p>
  </div>

  <!-- Popular features & disclaimer -->
  <h2 class="section-h abs" style="left:86px;top:733px">Popular Features</h2>
  <ul class="features">
    <li>Compare Pet Insurance: Tailplan Classic v Paw Pals Superior Plus</li>
    <li>Compare Lifetime Pet Insurance: Hart &amp; Lowe Plus vs Paw Pals Prestige</li>
    <li>Compare Lifetime Pet Insurance: Tailplan Classic vs Paw Pals Prestige</li>
    <li>Compare Lifetime Pet Insurance: Beyond Cover Premier vs Hart &amp; Lowe Premier</li>
    <li>Third Party Cover for Your Dogs: Beware of Loopholes!</li>
  </ul>
  <h2 class="section-h abs" style="left:86px;top:884px">Disclaimer</h2>
  <p class="disclaimer">Please note that pet insurance terms often change. Whilst we will do our best to keep this web-site up to date you must check with the appropriate insurer before making any decisions. If you find any mistakes on this website please do let us know so we can correct it for the benefit of future visitors. Many thanks!</p>

  <div class="divider"></div>

  <!-- Bio -->
  <h2 class="section-h bio-h abs" style="left:479px;top:731px">Bio</h2>
  <div class="bio-photo" role="img" aria-label="Portrait photo of the site owner"></div>
  <div class="bio-card">
    <div class="name">Owen Marsh <small>United Kingdom</small></div>
    <div class="role">Web Designer &amp; Owner <em>Bright Lantern</em><br>&amp; <em>K Cubed Studios</em></div>
    <div class="chips"><span style="width:24px;background:#e0452b"></span><span style="width:14px;background:#4aa14a"></span><span style="width:10px;background:#999"></span><span style="width:18px;background:#2a6db5"></span></div>
    <div style="font-size:3.5px;color:#777;margin-top:2px">Crafting clear sites for people who love their pets</div>
  </div>
  <div class="bio-text">
    <p>Critter Cover Surveys UK is an independent website dedicated to helping you find the best pet insurance policy for your pets.</p>
    <p>Here you will find unbiased detailed informa-tion about almost all the 205 policies current-ly available in the UK plus customer reviews by people who have actually claimed from the policy, premium surveys and more!</p>
    <p>We do not sell any pet insurance policies nor do.</p>
  </div>

  <!-- Footer -->
  <footer class="site-footer"></footer>

  <div class="fb-box">
    <div class="title">Find us on Friendbook</div>
    <div class="sep" style="top:13px"></div>
    <div class="mark"></div>
    <div class="page-name">Friendbook Builders</div>
    <div class="like">Like</div>
    <div class="sep" style="top:47px"></div>
    <div class="count">1,455,389 people like Friendbook Builders</div>
    <div class="faces" role="img" aria-label="Grid of follower profile pictures">
      <span></span><span></span><span></span><span></span><span></span>
      <span></span><span></span><span></span><span></span><span></span>
    </div>
    <div class="foot">Friendbook social plugin</div>
  </div>

  <div class="tw-box">
    <div class="tw-avatar" role="img" aria-label="Profile picture"></div>
    <div class="tw-head">Vet Review Circle<br><b>THE CRITTER COVER HANDBOOK 2015</b></div>
    <div class="tw-feed">
      <div class="tweet"><span class="who">Pet Insurance</span> Why your accountant could be costing you an arm and a leg <a>lnk.to/Qm4rTe</a><span class="meta">yesterday · reply · retweet · favorite</span></div>
      <div class="tweet"><span class="who">Pet Insurance</span> Buyers circle as duty calls <a>news.homeline.net/real-es...</a> via <a>@homelinenews</a><span class="meta">2 days ago · reply · retweet · favorite</span></div>
      <div class="tweet" style="border:0"><span class="who">Pet Insurance</span> Are you eligible for the Payroll Tax Rebate Scheme? Find out here <a>lnk.to/Wp7kAs</a><span class="meta">3 days ago · reply · retweet · favorite</span></div>
    </div>
    <div class="tw-foot">Chirper<span>Join the conversation</span></div>
  </div>

  <div class="follow-h">Follow Us</div>
  <div class="btn tw">Follow @CritterCoverUK</div>
  <div class="btn fb">Like</div>
  <div class="btn gp">Follow</div>
  <div class="flinks">About Us<br>Legal Information &amp; Disclaimers<br>Privacy Policy</div>

  <div class="band">Copyright © 2015. Critter Cover Surveys UK. All Right Reserved.</div>
</div>
</body>
</html>
```